IG ad to attract older men for better health #1

I want a bold headline Instagram Ad that coordinate with my website design with a racy sexy woman to attract men 45yrs old plus. See Two samples attached

Target Market(s)

Men 45 years old and older

Industry/Entity Type

Health And Wellness

Requirements
Must have
• eye catching appeal to men
Nice to have
• The copy to read
Kestrel61go is the headline at the top of the page. Then the copy reads...
"I want to seduce you to better health with a little T&A. Remove the excuses, provide ridiculously simple tips and advice to get you started on a path of lasting heath." Want more?

```html
<!DOCTYPE html>
<html lang="en">
<head>
<meta charset="utf-8">
<title>Kestrel61go – Instagram ad variations</title>
<link rel="stylesheet" href="https://fonts.googleapis.com/css2?family=Poppins:wght@400;500;600&family=Saira+Stencil+One&display=swap">
<style>
  :root {
    --page: #ffffff;
    --ink-dark: #141516;
    --yellow: #fcf835;
    --red: #cc1417;
    --teal: #10b4b4;
    --white: #ffffff;
    --skin-glow: #c98558;
    --skin-light: #a9643d;
    --skin-mid: #7a4127;
    --skin-dark: #4a2616;
    --garment: #0d0d0e;
  }
  * { margin: 0; padding: 0; box-sizing: border-box; }
  html, body {
    width: 1086px; height: 1200px; overflow: hidden;
    background: var(--page);
    font-family: "Poppins", sans-serif;
  }
  .ad {
    position: absolute;
    width: 466px; height: 520px;
    background: var(--ink-dark);
    overflow: hidden;
    color: var(--white);
  }
  .ad--a { left: 49px;  top: 54px; }
  .ad--b { left: 562px; top: 54px; }
  .ad--c { left: 49px;  top: 616px; }
  .ad--d { left: 562px; top: 616px; }

  .model-photo {
    position: absolute;
    left: 190px; top: 0; width: 276px; height: 463px;
    background:
      linear-gradient(180deg,
        transparent 0%, transparent 24%,
        rgba(13,13,14,.75) 30%, rgba(13,13,14,.75) 44%,
        transparent 50%, transparent 62%,
        rgba(13,13,14,.6) 67%, rgba(13,13,14,.6) 74%,
        transparent 80%),
      linear-gradient(90deg,
        var(--ink-dark) 0%,
        rgba(74,38,22,.7) 18%,
        var(--skin-mid) 35%,
        var(--skin-light) 55%,
        var(--skin-glow) 68%,
        var(--skin-light) 82%,
        var(--skin-dark) 100%);
  }

  .brand {
    position: absolute; left: 19px; top: 20px;
    font-family: "Saira Stencil One", sans-serif;
    font-size: 42px; line-height: 1;
    color: var(--yellow);
  }

  .pitch { position: absolute; left: 19px; font-size: 18px; line-height: 26px; font-weight: 500; }
  .ad--a .pitch { top: 102px; }
  .ad--b .pitch { top: 92px; line-height: 28px; font-weight: 400; }
  .ad--c .pitch { top: 26px; font-size: 21px; line-height: 30px; }
  .ad--d .pitch { top: 22px; font-size: 21px; line-height: 30px; color: var(--teal); }

  .tag { display: inline-block; padding: 0 6px; margin-left: -4px; }
  .tag--red { background: var(--red); color: var(--white); }
  .tag--pill { background: var(--yellow); color: var(--teal); border-radius: 14px; padding: 0 8px; margin-left: -7px; }

  .band { position: absolute; left: 0; }
  .band--red {
    top: 0; width: 466px; height: 136px;
    background: linear-gradient(90deg, var(--red) 0%, rgba(204,20,23,.85) 45%, rgba(204,20,23,.35) 80%, rgba(204,20,23,.1) 100%);
  }
  .band--yellow {
    top: 329px; width: 456px; height: 134px;
    background: linear-gradient(90deg, var(--yellow) 0%, var(--yellow) 35%, rgba(252,248,53,.6) 70%, rgba(252,248,53,.3) 100%);
  }

  .promise { position: absolute; left: 19px; font-size: 18.5px; line-height: 26px; font-weight: 600; }
  .ad--a .promise { top: 338px; color: var(--yellow); }
  .ad--b .promise, .ad--c .promise { top: 344px; line-height: 27.5px; color: var(--ink-dark); }
  .ad--d .promise { top: 334px; font-size: 18px; line-height: 27.5px; font-weight: 500; color: var(--white); }

  .cta {
    position: absolute; left: 0; top: 463px; width: 466px; height: 57px;
    padding-left: 19px; font-size: 26px; font-weight: 500; line-height: 57px;
  }
  .cta--yellow { background: var(--yellow); color: var(--ink-dark); }
  .cta--dark { background: var(--ink-dark); color: var(--white); }
  .cta--teal { background: var(--teal); color: var(--white); }
</style>
</head>
<body>

<section class="ad ad--a">
  <div class="model-photo" role="img" aria-label="Photo of a fit woman in black sports bra and briefs, hand on hip, on dark background"></div>
  <h1 class="brand">Kestrel61go</h1>
  <p class="pitch">I want to seduce you<br>to better health with<br><span class="tag tag--red">a little T&amp;A</span></p>
  <p class="promise">Remove the excuses,<br>provide ridiculously simple tips<br>and advice to get you started<br>on a path of lasting heath</p>
  <div class="cta cta--yellow">Want more?</div>
</section>

<section class="ad ad--b">
  <div class="model-photo" role="img" aria-label="Photo of a fit woman in black sports bra and briefs, hand on hip, on dark background"></div>
  <h1 class="brand">Kestrel61go</h1>
  <p class="pitch">I want to seduce you<br>to better health with<br>a little T&amp;A</p>
  <div class="band band--yellow"></div>
  <p class="promise">Remove the excuses,<br>provide ridiculously simple tips<br>and advice to get you started<br>on a path of lasting heath</p>
  <div class="cta cta--dark">Want more?</div>
</section>

<section class="ad ad--c">
  <div class="model-photo" role="img" aria-label="Photo of a fit woman in black sports bra and briefs, hand on hip, on dark background"></div>
  <div class="band band--red"></div>
  <p class="pitch">I want to seduce you<br>to better health with<br>a little T&amp;A</p>
  <div class="band band--yellow"></div>
  <p class="promise">Remove the excuses,<br>provide ridiculously simple tips<br>and advice to get you started<br>on a path of lasting heath</p>
  <div class="cta cta--dark">Want more?</div>
</section>

<section class="ad ad--d">
  <div class="model-photo" role="img" aria-label="Photo of a fit woman in black sports bra and briefs, hand on hip, on dark background"></div>
  <p class="pitch">I want to seduce you<br>to better health with<br><span class="tag tag--pill">a little T&amp;A</span></p>
  <p class="promise">Remove the excuses,<br>provide ridiculously simple tips<br>and advice to get you started<br>on a path of lasting heath</p>
  <div class="cta cta--teal">Want more?</div>
</section>

</body>
</html>
```